Flyer Design

We are a property company and need attractive flyers that will grab peoples attention. We want them to be bold but simple and not too busy. I attach a draft and also our logo. We will print in A5 size.
Thank you & I look forward to receiving designs.

It Company

```html
<!DOCTYPE html>
<html lang="en">
<head>
<meta charset="utf-8">
<title>Kora Developments – Subdivision Flyer</title>
<link rel="stylesheet" href="https://fonts.googleapis.com/css2?family=Cinzel:wght@500;600&family=Tinos:wght@400;700&display=swap">
<style>
  :root {
    --page-bg: #2a2a2a;
    --photo-light: #b47664;
    --photo-mid: #9a5c4b;
    --photo-dark: #7d4638;
    --wine: #7a1b15;
    --wine-deep: #6c1510;
    --gold: #dba55c;
    --white: #ffffff;
    --logo-panel: #e9e3d8;
    --logo-ink: #9a7348;
  }
  * { margin: 0; padding: 0; box-sizing: border-box; }
  html, body { width: 1200px; height: 1200px; overflow: hidden; }
  body { background: var(--page-bg); position: relative; }

  .flyer {
    position: absolute; left: 212px; top: 50px;
    width: 776px; height: 1100px;
    background: var(--wine); overflow: hidden;
  }
  .hero-photo {
    position: absolute; left: 0; top: 0; width: 100%; height: 780px;
    background: linear-gradient(160deg, var(--photo-light) 0%, var(--photo-mid) 55%, var(--photo-dark) 100%);
  }
  .contact-band {
    position: absolute; left: 0; top: 780px; width: 100%; height: 320px;
    background: var(--wine-deep);
  }
  .brand-plate {
    position: absolute; left: 300px; top: 170px; width: 370px; height: 270px;
    background: var(--logo-panel);
    box-shadow: 0 6px 14px rgba(0,0,0,.35);
    display: flex; align-items: center; justify-content: center; gap: 12px;
    z-index: 3;
  }
  .brand-mark { width: 16px; height: 16px; background: var(--logo-ink); }
  .brand-name {
    font-family: "Cinzel", serif; font-weight: 500; font-size: 32px;
    color: var(--logo-ink); letter-spacing: 1px;
  }
  .offer-panel {
    position: absolute; left: 78px; top: 410px; width: 670px; height: 480px;
    background: var(--wine);
    box-shadow: 0 6px 18px rgba(0,0,0,.35);
    padding: 70px 34px 0 38px;
    z-index: 2;
  }
  .questions { list-style: none; }
  .questions li {
    font-family: "Tinos", serif; font-weight: 700; font-size: 25px;
    color: var(--white); line-height: 1.2; margin-bottom: 8px;
    padding-left: 16px; position: relative;
  }
  .questions li::before {
    content: ""; position: absolute; left: 0; top: 9px;
    width: 7px; height: 7px; background: var(--white);
  }
  .divider { border: 0; border-top: 2px dotted var(--gold); margin: 22px 0; opacity: .8; }
  .headline {
    font-family: "Cinzel", serif; font-weight: 600; color: var(--gold);
    text-align: center; line-height: 1.1;
  }
  .headline .lead { display: block; font-size: 44px; }
  .headline .sub { display: block; font-size: 33px; }
  .headline .big { display: block; font-size: 52px; }

  .contact {
    position: absolute; left: 40px; top: 905px; width: 700px; z-index: 4;
    font-family: "Tinos", serif;
  }
  .contact-row { display: flex; align-items: center; gap: 12px; }
  .contact-row svg { flex: none; }
  .contact-main { justify-content: space-between; }
  .phone, .email, .web { color: var(--white); font-weight: 700; font-size: 30px; }
  .contact-note {
    color: var(--gold); font-weight: 700; font-size: 24px;
    text-align: center; margin: 18px 0 16px;
  }
</style>
</head>
<body>
  <main class="flyer">
    <div class="hero-photo" role="img" aria-label="Tinted photograph of a modern two-storey home with balcony"></div>
    <div class="contact-band"></div>

    <div class="brand-plate">
      <span class="brand-mark"></span>
      <span class="brand-name">Kora Developments</span>
    </div>

    <section class="offer-panel">
      <ul class="questions">
        <li>Are you a homeowner looking for financial freedom while been able to keep your own home?</li>
        <li>Are you struggling to pay your mortgage?</li>
      </ul>
      <hr class="divider">
      <h1 class="headline">
        <span class="lead">Kora specialise</span>
        <span class="sub">in subdivisions including</span>
        <span class="big">finance and</span>
        <span class="big">management.</span>
      </h1>
      <hr class="divider">
    </section>

    <section class="contact">
      <div class="contact-row contact-main">
        <div class="contact-row">
          <svg width="18" height="30" viewBox="0 0 18 30" aria-hidden="true">
            <rect x="1" y="1" width="16" height="28" rx="3" fill="none" stroke="#dba55c" stroke-width="2"/>
            <rect x="4" y="5" width="10" height="9" fill="#dba55c"/>
            <circle cx="9" cy="22" r="2" fill="#dba55c"/>
          </svg>
          <span class="phone">021 555 0147</span>
        </div>
        <div class="contact-row">
          <svg width="34" height="24" viewBox="0 0 34 24" aria-hidden="true">
            <rect x="1" y="1" width="32" height="22" fill="#dba55c"/>
            <path d="M1 1 L17 14 L33 1" fill="none" stroke="#6c1510" stroke-width="2"/>
          </svg>
          <span class="email">info@korasubdivisions.com</span>
        </div>
      </div>
      <p class="contact-note">for more information or to find out if your property<br>is suitable for subdivision in Auckland</p>
      <div class="contact-row" style="justify-content:center">
        <svg width="36" height="36" viewBox="0 0 36 36" aria-hidden="true">
          <g fill="none" stroke="#dba55c" stroke-width="2">
            <circle cx="18" cy="18" r="16"/>
            <ellipse cx="18" cy="18" rx="7" ry="16"/>
            <line x1="2" y1="18" x2="34" y2="18"/>
            <line x1="18" y1="2" x2="18" y2="34"/>
            <path d="M5 10 H31 M5 26 H31"/>
          </g>
        </svg>
        <span class="web">www.korasubdivisions.com</span>
      </div>
    </section>
  </main>
</body>
</html>
```